We need an attractive business card design that is modern and inviting. We like the blue and yellow (or gold) colors that are displayed with the logo. The business should communicate trust, experience, and integrity.

Target Market(s)

Residential and Commercial

Industry/Entity Type

Business

Contact Information for Business Card

Recessed Lighting
LED Retro Fit
Sign Repair
Alarms and Cameras
Mobile Home Services
24hr service calls

Font styles to use
Serif
Sans Serif

Colors
3176b5
0455a3
fece3e
fbee3e

Requirements
Must have
• Brannick Electric
• Owner: Marcus Brannick
• Licensed and Insured
• TECL #58731
Nice to have
• Exquisite Detail!!
• Over 20 years of experience
Should not have
• Nothing boring or traditional!!!

```html
<!DOCTYPE html>
<html lang="en">
<head>
<meta charset="utf-8">
<title>Brannick Electric – Business Card</title>
<link href="https://fonts.googleapis.com/css2?family=Montserrat:wght@400;500;600;700;800&display=swap" rel="stylesheet">
<style>
  :root {
    --bg: #2b2b2d;
    --card-black: #050505;
    --brand-blue: #0455a3;
    --band-blue: #0d5aa7;
    --brand-yellow: #fbee3e;
    --gold: #fece3e;
    --white: #ffffff;
  }
  * { margin: 0; padding: 0; box-sizing: border-box; }
  html, body {
    width: 1200px; height: 900px; overflow: hidden;
    background: var(--bg);
    font-family: "Montserrat", Arial, sans-serif;
  }
  .canvas { position: relative; width: 1200px; height: 900px; }
  .card {
    position: absolute;
    width: 700px; height: 400px;
    border-radius: 26px;
    background: var(--card-black);
    overflow: hidden;
    box-shadow: 0 14px 30px rgba(0,0,0,.45);
  }
  /* ---------- Services side ---------- */
  .card-services { left: 250px; top: 30px; text-align: center; }
  .services-brand {
    margin-top: 44px;
    display: flex; align-items: center; justify-content: center; gap: 14px;
    font-weight: 800; font-size: 34px; letter-spacing: 1px;
  }
  .brand-ring {
    width: 40px; height: 40px; border-radius: 50%;
    border: 5px solid var(--brand-blue);
  }
  .brand-word-blue { color: var(--brand-blue); }
  .brand-word-yellow { color: var(--brand-yellow); }
  .service-list {
    list-style: none; margin-top: 18px;
    color: var(--white); font-size: 17px; line-height: 25px; font-weight: 500;
  }
  .experience {
    margin-top: 18px; color: var(--white);
    font-size: 18px; font-weight: 500; letter-spacing: .5px;
  }
  .experience strong { color: var(--brand-yellow); font-weight: 700; }
  .licensed {
    margin-top: 8px; color: var(--white);
    font-size: 14px; font-weight: 600; letter-spacing: 2px;
  }

  /* ---------- Contact side ---------- */
  .card-contact { left: 250px; top: 470px; }
  .blue-band {
    position: absolute; inset: 0;
    background: var(--band-blue);
    clip-path: polygon(0 67%, 100% 42%, 100% 100%, 0 100%);
  }
  .contact-ring {
    position: absolute; right: 34px; top: 96px;
    width: 170px; height: 170px; border-radius: 50%;
    border: 9px solid var(--brand-blue);
    background: var(--card-black);
  }
  .contact-title {
    position: absolute; left: 44px; top: 38px;
    font-weight: 800; font-size: 50px; letter-spacing: 1px; line-height: 1;
  }
  .person { position: absolute; left: 44px; top: 122px; }
  .person-name { color: var(--white); font-size: 24px; font-weight: 700; letter-spacing: 1px; }
  .person-role { color: var(--brand-yellow); font-size: 15px; font-weight: 500; margin-top: 2px; }
  .license { color: var(--white); font-size: 18px; font-weight: 600; margin-top: 6px; }
  .license span { color: var(--brand-yellow); }
  .contact-details {
    position: absolute; left: 44px; top: 282px;
    color: var(--white); font-size: 15px; font-weight: 500; line-height: 20px;
  }
  .address { margin-bottom: 5px; }
  .contact-line { display: flex; align-items: center; gap: 10px; }
  .contact-line svg { width: 12px; height: 12px; flex: none; }
  .web-accent { color: var(--brand-yellow); font-weight: 600; }
</style>
</head>
<body>
<main class="canvas">

  <section class="card card-services">
    <div class="services-brand">
      <span class="brand-ring"></span>
      <span><span class="brand-word-blue">BRANNICK</span> <span class="brand-word-yellow">ELECTRIC</span></span>
    </div>
    <ul class="service-list">
      <li>Residential and Commercial</li>
      <li>Recessed Lighting</li>
      <li>LED Retro Fit</li>
      <li>Sign Repair</li>
      <li>Alarms and Cameras</li>
      <li>Mobile Home Services</li>
      <li>24hr service calls</li>
    </ul>
    <p class="experience"><strong>OVER 20</strong> YEARS OF EXPERIENCE</p>
    <p class="licensed">LICENSED AND INSURED</p>
  </section>

  <section class="card card-contact">
    <div class="blue-band"></div>
    <div class="contact-ring"></div>
    <h1 class="contact-title"><span class="brand-word-blue">BRANNICK</span> <span class="brand-word-yellow">ELECTRIC</span></h1>
    <div class="person">
      <p class="person-name">MARCUS BRANNICK</p>
      <p class="person-role">Owner</p>
      <p class="license"><span>TECL</span> #58731</p>
    </div>
    <div class="contact-details">
      <p class="address">4185 w Orchard Rd<br>Fairhaven mi 48210</p>
      <p class="contact-line">
        <svg viewBox="0 0 24 24" aria-hidden="true"><path fill="#fbee3e" d="M6.6 10.8a15 15 0 0 0 6.6 6.6l2.2-2.2a1 1 0 0 1 1-.25 11.4 11.4 0 0 0 3.6.57 1 1 0 0 1 1 1V20a1 1 0 0 1-1 1A17 17 0 0 1 3 4a1 1 0 0 1 1-1h3.5a1 1 0 0 1 1 1c0 1.25.2 2.45.57 3.57a1 1 0 0 1-.25 1z"/></svg>
        +330 2718-4093
      </p>
      <p class="contact-line">
        <svg viewBox="0 0 24 24" aria-hidden="true"><rect x="2" y="5" width="20" height="14" rx="2" fill="none" stroke="#fbee3e" stroke-width="2.4"/><path d="M3 6l9 7 9-7" fill="none" stroke="#fbee3e" stroke-width="2.4"/></svg>
        info@brannickelectric.com
      </p>
      <p class="contact-line">
        <svg viewBox="0 0 24 24" aria-hidden="true"><circle cx="12" cy="12" r="10" fill="#fbee3e"/></svg>
        <span>www.<span class="web-accent">brannickelectric</span>.com</span>
      </p>
    </div>
  </section>

</main>
</body>
</html>
```